Header Design

I would like a new header design for my website - www.nestmarla.com.

I am a Realtor and the header should reflect that and complement the theme.

The attached logo needs to be included and the information that is already there. Also, the colors need to match.

Marla Quinby
Connecting you to the Los Angeles real estate scene.

Industry/Entity Type

Realtor

```html
<!DOCTYPE html>
<html lang="en">
<head>
<meta charset="UTF-8">
<title>Marla Quinby – Los Angeles Real Estate Header</title>
<link rel="stylesheet" href="https://fonts.googleapis.com/css2?family=Nunito:wght@800&family=Arimo:wght@400&display=swap">
<style>
  :root {
    --frame-purple: #3a2647;
    --nav-purple: #33213f;
    --divider: #6d5a78;
    --text-white: #ffffff;
    --city-dark: #2a1a16;
    --city-mid: #6b4424;
    --city-glow: #b57a3c;
  }
  html, body {
    margin: 0;
    padding: 0;
    overflow: hidden;
  }
  .site-header {
    position: relative;
    width: 1200px;
    height: 172px;
    background: var(--frame-purple);
    overflow: hidden;
    font-family: "Arimo", Arial, sans-serif;
  }
  .brand-mark {
    position: absolute;
    left: 22px;
    top: 28px;
    width: 118px;
    display: flex;
    flex-direction: column;
    align-items: flex-start;
    gap: 8px;
  }
  .brand-mark__square {
    width: 30px;
    height: 30px;
    background: var(--text-white);
  }
  .brand-mark__name {
    font-family: "Nunito", Arial, sans-serif;
    font-weight: 800;
    font-size: 18px;
    line-height: 20px;
    color: var(--text-white);
  }
  .brand-divider {
    position: absolute;
    left: 153px;
    top: 6px;
    width: 2px;
    height: 127px;
    background: var(--divider);
  }
  .city-banner {
    position: absolute;
    left: 156px;
    top: 6px;
    width: 1039px;
    height: 127px;
    background:
      radial-gradient(ellipse 40% 70% at 55% 75%, var(--city-glow) 0%, rgba(181,122,60,0) 100%),
      linear-gradient(180deg, var(--city-mid) 0%, var(--city-dark) 35%, var(--city-mid) 70%, var(--city-glow) 100%);
  }
  .banner-title {
    position: absolute;
    left: 164px;
    top: 14px;
    margin: 0;
    font-family: "Nunito", Arial, sans-serif;
    font-weight: 800;
    font-size: 58px;
    line-height: 66px;
    color: var(--text-white);
  }
  .banner-tagline {
    position: absolute;
    left: 166px;
    top: 78px;
    margin: 0;
    font-family: "Nunito", Arial, sans-serif;
    font-weight: 800;
    font-size: 22px;
    line-height: 26px;
    color: var(--text-white);
  }
  .main-nav {
    position: absolute;
    left: 0;
    top: 133px;
    width: 1200px;
    height: 39px;
    background: var(--nav-purple);
  }
  .main-nav a {
    position: absolute;
    top: 10px;
    font-size: 17px;
    line-height: 20px;
    color: var(--text-white);
    text-decoration: none;
    white-space: nowrap;
  }
</style>
</head>
<body>
  <header class="site-header">
    <div class="brand-mark">
      <div class="brand-mark__square"></div>
      <div class="brand-mark__name">Marla<br>Quinby</div>
    </div>
    <div class="brand-divider"></div>
    <div class="city-banner" role="img" aria-label="Night skyline of downtown Los Angeles with glowing city lights"></div>
    <h1 class="banner-title">Marla Quinby</h1>
    <p class="banner-tagline">Connecting you to the Los Angeles real estate scene</p>
    <nav class="main-nav">
      <a href="#" style="left:24px">Home</a>
      <a href="#" style="left:106px">About Marla</a>
      <a href="#" style="left:230px">Home Search Central</a>
      <a href="#" style="left:434px">Search By Community</a>
      <a href="#" style="left:642px">Buyers</a>
      <a href="#" style="left:733px">Sellers</a>
      <a href="#" style="left:823px">Renters</a>
      <a href="#" style="left:922px">Market Reports</a>
      <a href="#" style="left:1078px">Contact Me</a>
    </nav>
  </header>
</body>
</html>
```